Specialty Chemical Product Line Card Revamp

I need a new digital brochure for our product catalog of various chemicals. This will be sent to my customers as a digital file or printed on flat paper (not a folded brochure). I have included the OLD brochure (Tobin Chemical Line Card document) and the new categories that I want used instead (Line Card Categories document). I also included our logo and other photos. I would like the new brochure to be more modern and attention-grabbing

Target Market(s)

Product Manufacturers

Industry/Entity Type

Chemical Product

Font styles to use
Serif
Sans Serif

Requirements
Must have
• Product Category Headers. Company Logo
Nice to have
• Incorporate the attached photos. Use similar colors as the logo. Fit on 2 pages
Should not have
• Cannot be more than 3 pages.

```html
<!DOCTYPE html>
<html lang="en">
<head>
<meta charset="utf-8">
<title>Tobin Chemical – Product Line Card</title>
<link rel="stylesheet" href="https://fonts.googleapis.com/css2?family=Open+Sans:wght@600;700;800&family=Cinzel:wght@600&display=swap">
<style>
:root{
  --green:#3f9e26;
  --green-dark:#2a7a18;
  --green-light:#6cc24a;
  --ink:#1d1f22;
  --navy:#1f2b5e;
  --paper:#ffffff;
  --mist:#eef2f4;
  --photo-blue:#cfe2ee;
  --photo-steel:#9fb5bd;
}
*{margin:0;padding:0;box-sizing:border-box}
html,body{width:1200px;height:4712px;overflow:hidden;background:var(--paper)}
body{position:relative;font-family:"Open Sans",Arial,sans-serif;color:var(--ink)}
.page{position:absolute;left:0;width:1200px;overflow:hidden;background:var(--paper)}
.page-one{top:0;height:1570px}
.page-two{top:1590px;height:1450px}
.page-three{top:3060px;height:1652px}
.page-backdrop{position:absolute;left:0;right:0;background:linear-gradient(180deg,rgba(238,242,244,0) 0%,#e9eef0 45%,#dfe6e8 100%)}
.page-one .page-backdrop{top:1050px;bottom:40px}
.page-two .page-backdrop{top:900px;bottom:40px}
.page-top-rule{position:absolute;top:0;left:0;right:0;height:18px;background:linear-gradient(180deg,#d9dee0,#f4f6f7)}
.page-top-rule::after{content:"";position:absolute;left:0;right:0;bottom:0;height:5px;background:linear-gradient(90deg,var(--green-dark),var(--green-light),var(--green-dark))}
.hero-photo{position:absolute;top:0;left:0;width:1200px;height:395px;background:linear-gradient(135deg,#e8f1f7 0%,var(--photo-blue) 40%,#f4f8fb 60%,#b9d3e2 100%)}
.hero-rule{position:absolute;top:395px;left:0;right:0;height:6px;background:linear-gradient(90deg,var(--green-dark),var(--green-light),var(--green-dark))}
.brand-band{position:absolute;left:0;right:0;top:140px;height:140px;background:rgba(255,255,255,.82);display:flex;align-items:center;justify-content:center}
.brand-name{font-family:"Cinzel",Georgia,serif;font-weight:600;font-size:82px;color:var(--navy);letter-spacing:1px}
.site-band{position:absolute;left:0;right:0;bottom:0;height:40px;background:linear-gradient(90deg,var(--green-dark),var(--green),var(--green-dark));color:#fff;font-size:15px;font-weight:700;letter-spacing:3px;display:flex;align-items:center;justify-content:center}
.category{position:absolute;width:525px}
.category-head{position:relative;height:40px;margin-left:10px;border-radius:20px;background:linear-gradient(90deg,var(--green-light),var(--green) 45%,var(--green-dark));display:flex;align-items:center;padding-left:72px;color:#fff;font-weight:800;font-size:22px;letter-spacing:.5px;text-transform:uppercase}
.category-head .badge{position:absolute;left:-12px;top:-10px;width:60px;height:60px;border-radius:50%;border:4px solid #fff;background:radial-gradient(circle at 40% 35%,#c8d6dc,#7f949c);box-shadow:0 1px 3px rgba(0,0,0,.3)}
.item-columns{display:grid;grid-template-columns:1fr 1fr;column-gap:22px;padding:14px 0 0 14px}
.item-columns ul{list-style:none}
.item-columns li{font-size:14.5px;font-weight:600;line-height:21px;padding-bottom:6px}
.compact .item-columns li{padding-bottom:4px}
.left-col{left:50px}
.right-col{left:620px}
.solvents{top:440px}
.alcohols{top:440px}
.acids{top:922px}
.oils{top:50px}
.solids{top:50px}
.metals{top:316px}
.sodium{top:693px}
.amines{top:1230px}
.ammonium{top:150px}
.function{top:150px}
.misc{top:407px}
.closing-photo{position:absolute;left:0;right:0;top:930px;bottom:0;background:linear-gradient(180deg,rgba(255,255,255,1) 0%,#dfe7e4 18%,#a9bcb6 60%,#7f958e 100%)}
.closing-brand{position:absolute;left:0;right:0;top:1060px;height:140px;display:flex;align-items:center;justify-content:center;background:rgba(255,255,255,.6)}
.closing-phone{position:absolute;left:0;right:0;top:1330px;text-align:center;color:#fff;font-weight:700;font-size:64px;letter-spacing:1px}
.closing-site{position:absolute;left:0;right:0;top:1440px;text-align:center;color:#fff;font-weight:700;font-size:30px;letter-spacing:5px}
</style>
</head>
<body>

<section class="page page-one">
  <div class="hero-photo" role="img" aria-label="Laboratory glassware with blue liquids on a bright bench"></div>
  <div class="brand-band"><span class="brand-name">Tobin Chemical</span></div>
  <div class="hero-rule"></div>
  <div class="page-backdrop" role="img" aria-label="Faint view of the company warehouse building"></div>

  <div class="category left-col solvents">
    <div class="category-head"><span class="badge"></span>Solvents</div>
    <div class="item-columns">
      <ul>
        <li>Acetate, N-butyl</li><li>Acetate, N-propyl</li><li>Acetone</li><li>Aliphatic Solvents</li><li>Amyl Acetate</li><li>Aromatic Solvents</li><li>Butyl Acetate</li><li>Cyclohexane</li><li>Cyclohexanone</li><li>DB Acetate</li><li>DE Acetate</li><li>Diisobutyl Ketone (DIBK)</li><li>Dimethylformamide</li><li>EB Acetate</li><li>Ethyl Acetate</li><li>Ethyl Ether, Reagent</li><li>Ethylene Dichloride</li><li>Heptane</li><li>Hexane</li><li>Isobutyl Acetate</li><li>Isophorone</li><li>Isopropyl Acetate</li><li>Ketones</li><li>Methyl Amyl Ketone</li><li>Methyl Glycol Ether (EM)</li><li>Methyl Diglycol (DM)</li>
      </ul>
      <ul>
        <li>Methyl Ethyl Ketone (MEK)</li><li>Methyl Isoamyl Ketone</li><li>Methyl Isobutyl Ketone (MIBK)</li><li>Methyl Salicylate</li><li>Methylene Chloride</li><li>Mineral Spirits, Low odor</li><li>Mineral Spirits, Odorless</li><li>Mineral Spirits, Rule 66</li><li>Mineral Spirits, Stoddard Solvent</li><li>n-Butyl Pyrrolidone</li><li>n-Propyl Bromide</li><li>Perchloroethylene</li><li>Petroleum Ether</li><li>PM Acetate</li><li>Fast Dry Solvent</li><li>Sodium Acetate</li><li>Solvent 100</li><li>Solvent 142</li><li>Solvent 150</li><li>Tetrahydrofuran</li><li>Toluene</li><li>Trichloroethylene</li><li>Typewash</li><li>Xylene</li>
      </ul>
    </div>
  </div>

  <div class="category right-col alcohols">
    <div class="category-head"><span class="badge"></span>Alcohols</div>
    <div class="item-columns">
      <ul>
        <li>Butanol</li><li>Cyclohexanol</li><li>Denatured Alcohol</li><li>Diacetone Alcohol</li><li>DBE</li><li>Diethylene Glycol</li><li>Dipropylene Glycol</li><li>Thermfrost</li><li>Thermsol SR-1</li><li>Ethyl Alcohol 190 Proof</li><li>Ethyl Alcohol 200 Proof</li><li>Ethylene Glycol</li><li>Glycerine</li><li>Glycol Ether Acetates</li>
      </ul>
      <ul>
        <li>Hexylene Glycol</li><li>Isobutyl Alcohol</li><li>Isopropyl Alcohol</li><li>Methanol</li><li>Methyl Amyl Alcohol</li><li>n-Butyl Alcohol</li><li>n-Propyl Alcohol</li><li>Polyethylene Glycols</li><li>Propylene Glycol, Industrial</li><li>Propylene Glycol, USP</li><li>Secondary Butyl Alcohol</li><li>Sorbitol</li><li>Surfactols</li><li>Tetraethylene Glycol</li>
      </ul>
    </div>
  </div>

  <div class="category right-col acids">
    <div class="category-head"><span class="badge"></span>Acids</div>
    <div class="item-columns">
      <ul>
        <li>Acetic Acid 28%, 56%, 75%, 80%</li><li>Acetic Acid Glacial 99.5%</li><li>Acetic Acid, Reagent</li><li>Boric Acid</li><li>Chromic Acid</li><li>Citric Acid, USP</li><li>Citric Acid, Liquid</li><li>EDTA (Chelate)</li><li>Fluoboric Acid 48-50%</li><li>Formic Acid</li><li>Glacial Acetic Acid</li><li>Gluconic Acid</li><li>Glycolic Acid</li><li>Hydrochloric Acid</li><li>Hydrochloric Acid Reagent</li>
      </ul>
      <ul>
        <li>Hydrofluoric Acid</li><li>Hydrofluosilicic Acid 25%</li><li>Lactic Acid</li><li>Muriatic Acid 18°, 20°, 22°</li><li>Muriatic Acid, Inhibited</li><li>Nitric Acid</li><li>Nitric Acid, Reagent</li><li>Oxalic Acid</li><li>Phosphoric Acid 75%, 85%, Tech</li><li>Phosphoric Acid, Reagent</li><li>Sorbic Acid</li><li>Sulfamic Acid</li><li>Sulfuric Acid 66°</li><li>Sulfuric Acid, Reagent</li>
      </ul>
    </div>
  </div>

  <div class="site-band">www.tobinchemical-supply.com</div>
</section>

<section class="page page-two compact">
  <div class="page-top-rule"></div>
  <div class="page-backdrop" role="img" aria-label="Faint view of the company warehouse building"></div>

  <div class="category left-col oils">
    <div class="category-head"><span class="badge"></span>Oils</div>
    <div class="item-columns">
      <ul>
        <li>Naphthenic Base Oil</li><li>D-Limonene</li><li>Kerosene</li><li>Mineral Seal Oil</li><li>Mop Oil</li><li>Naphtha, V M &amp; P</li><li>Naphthenic Oils</li>
      </ul>
      <ul>
        <li>Pine Oil</li><li>V M &amp; P Naphtha</li><li>Vanishing Oil</li><li>Way Lubricants</li><li>White Kerosene</li><li>White Oils</li>
      </ul>
    </div>
  </div>

  <div class="category right-col solids">
    <div class="category-head"><span class="badge"></span>Solids</div>
    <div class="item-columns">
      <ul>
        <li>Activated Carbon</li><li>Anhydrous Ammonia</li><li>Aluminum Sulfate</li><li>Barium Carbonate</li><li>Bicarbonate of Soda</li><li>CCH Granular 65% (Cal-Hypo)</li><li>Calcium Bromide</li><li>Calcium Chloride, flake or pellets</li><li>Calcium Nitrate</li><li>Caustic Potash, flake</li><li>Caustic Soda, beads or flake</li><li>Citric Acid, USP</li><li>Copper Cyanide</li><li>Copper Sulfate, crystal</li><li>Dipotassium Phosphate, FCC</li><li>Disodium Phosphate, FCC</li><li>Epsom Salts</li><li>Manganese Sulfate, dry</li>
      </ul>
      <ul>
        <li>Muriate of Potash</li><li>Nickel Chloride, dry</li><li>Nickel Sulfate, salt</li><li>Oil Absorbent Granules</li><li>Calcium Pellets</li><li>Rochelle Salts</li><li>Rock Salt</li><li>Sodium Bisulfate, Anhy G.B.S.</li><li>Sodium Citrate, USP granular</li><li>Sodium Metasilicate, Anhy.</li><li>Sodium Sulfate, Anhydrous</li><li>Sodium Thiosulfate, dry</li><li>Sodium Tripolyphosphate, Anhy, Gran, Lite</li><li>Sodium Tripolyphosphate, Anhy, Gran, Tech</li><li>Tetra Potassium Pyro Phosphate, Gran, Tech</li><li>Zinc Dust</li>
      </ul>
    </div>
  </div>

  <div class="category left-col metals">
    <div class="category-head"><span class="badge"></span>Metals &amp; Salts</div>
    <div class="item-columns">
      <ul>
        <li>Aluminum Chloride</li><li>Aluminum Sulfate</li><li>Bicarbonate of Soda</li><li>Borax 5 mol, pentahydrate</li><li>Cadmium Oxide</li><li>Calcium Acetate</li><li>Calcium Borate</li><li>Calcium Chloride, liquid</li><li>Calcium Nitrate</li><li>Chlorine, gas, liquid or dry</li><li>Copper Anodes</li><li>Copper Cyanide</li><li>Copper Sulfate, Crystal</li><li>DOBSA</li><li>Dipotassium Phosphate, FCC</li><li>Epsom Salts</li><li>Ferric Chloride DWG</li><li>Ferric Sulfate</li><li>Ferrous Sulfate (Copperas)</li><li>Iron Phosphates</li><li>Lime, hydrated</li><li>Lithium Carbonate</li><li>Magnesium Chloride</li><li>Magnesium Hydroxide</li><li>Magnesium Oxide</li><li>Magnesium Sulfate</li><li>Manganese Carbonate</li><li>Manganese Sulfate, liquid or dry</li><li>Monoaluminum Phosphate</li><li>Monopotassium Phosphate</li>
      </ul>
      <ul>
        <li>Nickel Acetate</li><li>Nickel Anodes</li><li>Nickel Chloride, solution</li><li>Nickel Fluoborate</li><li>Nickel Sulfate, solution</li><li>Phosphates</li><li>Polyphosphates</li><li>Potassium Copper Cyanide</li><li>Potassium Alum</li><li>Potassium Carbonate</li><li>Potassium Chloride</li><li>Potassium Cyanide</li><li>Potassium Permanganate</li><li>Rochelle Salts</li><li>Rock Salt</li><li>Soda Ash</li><li>Soap</li><li>Stannous Fluoborate, solution</li><li>Stannous Sulfate</li><li>Sulfur</li><li>Sulfur Dioxide</li><li>Tetra Potassium Pyro Phosphate, FCC</li><li>Tolytriazole</li><li>Tricalcium Phosphate</li><li>Glassy Phosphate</li><li>Zinc Anodes</li><li>Zinc Chloride</li><li>Zinc Cyanide</li><li>Zinc Oxide</li>
      </ul>
    </div>
  </div>

  <div class="category right-col sodium">
    <div class="category-head"><span class="badge"></span>Sodium Compounds</div>
    <div class="item-columns">
      <ul>
        <li>Disodium Phosphate, FCC</li><li>Monosodium Phosphate</li><li>Sodium Acetate</li><li>Sodium Benzoate</li><li>Sodium Bichromate</li><li>Sodium Bisulfate, Anhy G.B.S.</li><li>Sodium Bisulfite, liquid</li><li>Sodium Bicarbonate</li><li>Sodium Bifluoride</li><li>Sodium Cyanide</li><li>Sodium Chlorate</li><li>Sodium Citrate, USP granular</li><li>Sodium Fluoride</li><li>Sodium Gluconate</li><li>Sodium Hexametaphosphate, Tech</li><li>Sodium Hexametaphosphate, Food grade</li><li>Sodium Hydrosulfite</li><li>Sodium Hypochlorite</li><li>Sodium Metasilicate, Anhy.</li><li>Sodium Metasilicate, Pent, Crystal</li>
      </ul>
      <ul>
        <li>Sodium Molybdate</li><li>Sodium Nitrate</li><li>Sodium Nitrite</li><li>Sodium Percarbonate</li><li>Sodium Permanganate</li><li>Sodium Persulfate</li><li>Sodium Acid Pyrophosphate</li><li>Sodium Silicate</li><li>Sodium Silicofluoride</li><li>Sodium Sulfide</li><li>Sodium Sulfate</li><li>Sodium Sulfate, Anhydrous</li><li>Sodium Thiosulfate, liquid or dry</li><li>Sodium Tripolyphosphate, Anhy, Gran, Lite</li><li>Sodium Tripolyphosphate, Anhy, Gran, Tech</li><li>Tetra Sodium Pyro Phosphate, FCC</li><li>Trisodium Phosphate</li>
      </ul>
    </div>
  </div>

  <div class="category left-col amines">
    <div class="category-head"><span class="badge"></span>Amines</div>
    <div class="item-columns">
      <ul>
        <li>Cyclohexylamine</li><li>DEA 99%</li><li>Diethylamine</li><li>Diethylethanolamine</li><li>Dimethyl Ethanolamine</li>
      </ul>
      <ul>
        <li>Ethylenediamine</li><li>Monoethanolamine</li><li>Morpholine</li><li>Triethylolamine 85%, 99%</li><li>Triethylamine</li>
      </ul>
    </div>
  </div>

  <div class="site-band">www.tobinchemical-supply.com</div>
</section>

<section class="page page-three">
  <div class="page-top-rule"></div>
  <div class="closing-photo" role="img" aria-label="Rows of chemical drums stored in a warehouse"></div>

  <div class="category left-col ammonium">
    <div class="category-head"><span class="badge"></span>Ammonium Compounds</div>
    <div class="item-columns">
      <ul>
        <li>Ammonium Bicarbonate</li><li>Ammonium Chloride, Treated or Untreated</li><li>Ammonium Bifluoride</li><li>Ammonium Hydroxide 21, 26</li><li>Ammonium Hydroxide, Reagent</li>
      </ul>
      <ul>
        <li>Ammonium Nitrate</li><li>Ammonium Persulfate</li><li>Ammonium Sulfate</li><li>Anhydrous Ammonia</li><li>Monoammonium Phosphate</li>
      </ul>
    </div>
  </div>

  <div class="category right-col function">
    <div class="category-head"><span class="badge"></span>By Function</div>
    <div class="item-columns">
      <ul>
        <li>Antifoams</li><li>Antifreeze</li><li>Blanket/Roller Wash</li><li>Chelating Agents</li><li>Chlorinated Solvents</li><li>Cleaners, Floor, Metal, Soak, Steam</li><li>Coolants</li><li>Corrosion Inhibitors</li><li>Cutting Oils</li><li>Dechlorinators</li><li>Defoamers</li><li>Degreasing Solvents</li><li>Deicers</li><li>Descaling Acid</li><li>Electro Cleaners</li><li>Filter Powders</li><li>Floor Adsorbents</li><li>Foam Control</li><li>Form Oils</li><li>Gear Oils</li><li>Heat Transfer Fluids</li><li>Hydraulic Fluids</li><li>Inhibited Glycol Fluids</li><li>Lacquer Reducers</li>
      </ul>
      <ul>
        <li>Lacquer Thinners</li><li>Laboratory Chemicals</li><li>Metal Cleaners</li><li>Metal Conditioners</li><li>Metalworking Lubricants</li><li>Nonionic Surfactants</li><li>Paint Strippers</li><li>Paint Thinners</li><li>Process Oils</li><li>Reagent Acids</li><li>Reagent Solvents</li><li>Rubber Rejuvenator</li><li>Rust Proofers</li><li>Safety Absorbent</li><li>Safety Solvents</li><li>Soak Cleaners</li><li>Soluble Oils</li><li>Steam Cleaners</li><li>Surfactants</li><li>Synthetic Coolants</li><li>Thinners</li><li>Waste Water Treatment Solutions</li><li>Water Soluble Oils</li><li>Wetting Agents</li>
      </ul>
    </div>
  </div>

  <div class="category left-col misc">
    <div class="category-head"><span class="badge"></span>Miscellaneous</div>
    <div class="item-columns">
      <ul>
        <li>All Purpose Cleaner</li><li>Bleach</li><li>Polywax</li><li>Caustic Soda Liquid 50%, Diaphragm Grade</li><li>Caustic Soda Liquid, Membrane Grade</li><li>Distilled Water</li><li>Thermfrost</li><li>Thermsol</li>
      </ul>
      <ul>
        <li>Formaldehyde 37%</li><li>Hydrogen Peroxide, Tech, Food Grade</li><li>Silikol (Potassium Silicate)</li><li>Rapid Dry</li><li>Soaps</li><li>Polyols</li><li>Urea</li><li>Windshield Washer Solvent</li>
      </ul>
    </div>
  </div>

  <div class="closing-brand"><span class="brand-name">Tobin Chemical</span></div>
  <div class="closing-phone">(555) 014-2277</div>
  <div class="closing-site">www.tobinchemical-supply.com</div>
</section>

</body>
</html>
```